Small Business coaching and services company

Need a powerpoint template design for a company that provides Human Resources services as well sales and business coaching.

```html
<!DOCTYPE html>
<html lang="en">
<head>
<meta charset="utf-8">
<title>Corvala – Presentation Template</title>
<link href="https://fonts.googleapis.com/css2?family=Poppins:wght@400;500;600;700&display=swap" rel="stylesheet">
<style>
:root{
  --purple:#5b2d8e;
  --purple-deep:#3a1a63;
  --orange:#f5a623;
  --ink:#1c1c1e;
  --text:#3c3c40;
  --muted:#8a8a90;
  --bar-gray:#4a4a4e;
  --page:#d2d2d5;
  --rule:#e6e6ea;
  --white:#ffffff;
}
*{box-sizing:border-box;margin:0;padding:0}
html,body{width:1200px;height:3125px;overflow:hidden}
body{background:var(--page);font-family:"Poppins",Arial,sans-serif;color:var(--text);position:relative}

.brand{position:absolute;display:flex;align-items:center;gap:5px;font-weight:700;letter-spacing:-.2px;white-space:nowrap}
.brand .dot{display:block;border-radius:50%;background:var(--orange)}
.top-brand{right:38px;top:44px;font-size:30px;color:var(--purple)}
.top-brand .dot{width:28px;height:28px}

.hero{position:absolute;left:70px;top:120px;transform:scale(1.8828);transform-origin:0 0;box-shadow:0 8px 30px rgba(0,0,0,.18)}

.slide{position:absolute;width:563px;height:316px;overflow:hidden;background:var(--white)}
.col-l{left:28px}.col-r{left:609px}
.abs{position:absolute}
.photo{position:absolute}

/* title slides */
.t-brand{left:44px;top:52px;font-size:19px}
.t-brand .dot{width:18px;height:18px}
.t-title{position:absolute;left:44px;top:120px;font-size:27px;font-weight:700;line-height:31px}
.t-rule{position:absolute;left:44px;top:190px;width:92px;height:3px;background:var(--orange)}
.t-sub{position:absolute;left:44px;top:201px;font-size:9.5px}
.t-date{position:absolute;left:44px;top:237px;font-size:6.5px;font-weight:500;letter-spacing:.3px}
.t-foot{position:absolute;left:0;bottom:0;width:100%;height:19px;font-size:5.5px;text-align:center;line-height:19px}

.dark{background:#000;color:var(--white)}
.dark .t-foot{background:var(--white);color:var(--ink)}
.light .t-title{color:var(--purple)}
.light .t-sub,.light .t-date{color:var(--ink)}
.light .t-foot{background:#4d4d50;color:var(--white)}
.duo{background:var(--purple);color:var(--white)}
.duo .t-foot{background:#4d4d50}

/* content slide chrome */
.foot-brand{left:15px;top:284px;font-size:10px;color:var(--purple)}
.foot-brand .dot{width:10px;height:10px}
.foot-rule{position:absolute;left:100px;right:80px;top:293px;height:4px;background:#f1f1f3;border-radius:2px}
.copy{position:absolute;right:34px;top:288px;font-size:4.5px;color:var(--muted)}
.pg{position:absolute;right:14px;top:287px;width:10px;height:10px;border-radius:50%;background:var(--purple);color:#fff;font-size:5px;line-height:10px;text-align:center;font-weight:600}

.h-center{position:absolute;left:0;width:100%;top:20px;text-align:center;font-size:17.5px;font-weight:600;color:var(--ink)}
.h-left{font-size:17.5px;font-weight:600;color:var(--ink);line-height:21px}
.p{font-size:6.4px;line-height:8px;color:var(--text)}
.p-c{text-align:center}
.name{font-size:10px;font-weight:600;color:var(--purple);line-height:11px}
.role{font-size:6.5px;color:var(--orange)}
.head{font-size:8px;font-weight:600;color:var(--ink)}
.orange-h{font-size:10px;font-weight:600;color:var(--orange);line-height:11px}
.list{font-size:5.8px;line-height:8.5px;color:var(--text);list-style:none}
.list li::before{content:"•";margin-right:4px;color:var(--text)}

.round{position:absolute;border-radius:50%;display:flex;align-items:center;justify-content:center}
.num{position:absolute;width:38px;height:38px;border-radius:50%;color:#fff;font-size:19px;font-weight:600;display:flex;align-items:center;justify-content:center}

.card{position:absolute;top:78px;width:125px;height:185px;border:1px solid #d9d9de;border-radius:4px;padding:8px 6px}
.card-top{display:flex;align-items:center;gap:4px;margin-bottom:8px}
.card-top span{font-size:8px;font-weight:600;line-height:8.5px}
.card .head{font-size:7px;margin:4px 0 2px}
.card .list{font-size:5px;line-height:7px;padding-left:6px}

.box-num{position:absolute;left:258px;width:84px;height:61px;background:var(--purple);color:#fff;font-size:24px;font-weight:600;display:flex;align-items:center;justify-content:center}
.box-txt{position:absolute;left:357px;width:180px;font-size:5.4px;line-height:7px;color:var(--text);border-bottom:1px solid var(--rule);padding-bottom:5px}
</style>
</head>
<body>

<div class="brand top-brand"><span class="dot"></span>Corvala</div>

<!-- hero: dark title slide -->
<section class="slide dark hero">
  <div class="photo" role="img" aria-label="Handshake over a signed contract, tinted purple" style="left:230px;top:0;width:333px;height:297px;background:linear-gradient(90deg,rgba(0,0,0,1) 0%,rgba(58,26,99,.85) 35%,rgba(106,72,160,.8) 65%,rgba(200,192,218,.9) 100%)"></div>
  <div class="brand t-brand" style="color:var(--white)"><span class="dot"></span>Corvala</div>
  <h1 class="t-title">Presentation<br>Title Goes Here!</h1>
  <div class="t-rule"></div>
  <p class="t-sub">Sub-Title of Presentation Goes Here</p>
  <p class="t-date">Sunday, February 5, 2023</p>
  <p class="t-foot">© 2023 Corvala.</p>
</section>

<!-- row 1 -->
<section class="slide dark col-l" style="top:769px">
  <div class="photo" role="img" aria-label="Handshake over a signed contract, tinted purple" style="left:230px;top:0;width:333px;height:297px;background:linear-gradient(90deg,rgba(0,0,0,1) 0%,rgba(58,26,99,.85) 35%,rgba(106,72,160,.8) 65%,rgba(200,192,218,.9) 100%)"></div>
  <div class="brand t-brand" style="color:var(--white)"><span class="dot"></span>Corvala</div>
  <h2 class="t-title">Presentation<br>Title Goes Here!</h2>
  <div class="t-rule"></div>
  <p class="t-sub">Sub-Title of Presentation Goes Here</p>
  <p class="t-date">Sunday, February 5, 2023</p>
  <p class="t-foot">© 2023 Corvala.</p>
</section>

<section class="slide light col-r" style="top:769px">
  <div class="photo" role="img" aria-label="Handshake over a signed contract, soft white fade" style="left:220px;top:0;width:343px;height:297px;background:linear-gradient(90deg,#fff 0%,#eeeef2 40%,#d9dbe3 75%,#c5c9d4 100%)"></div>
  <div class="brand t-brand" style="color:var(--purple)"><span class="dot"></span>Corvala</div>
  <h2 class="t-title">Presentation<br>Title Goes Here!</h2>
  <div class="t-rule"></div>
  <p class="t-sub">Sub-Title of Presentation Goes Here</p>
  <p class="t-date">Sunday, February 5, 2023</p>
  <p class="t-foot">© 2023 Corvala.</p>
</section>

<!-- row 2 -->
<section class="slide duo col-l" style="top:1104px">
  <div class="photo" role="img" aria-label="Handshake over a signed contract, tinted orange" style="left:200px;top:0;width:363px;height:297px;background:linear-gradient(90deg,rgba(91,45,142,1) 0%,#a56a6e 35%,#e6a23a 65%,#efcf95 100%)"></div>
  <div class="brand t-brand" style="color:var(--white)"><span class="dot"></span>Corvala</div>
  <h2 class="t-title">Presentation<br>Title Goes Here!</h2>
  <div class="t-rule"></div>
  <p class="t-sub">Sub-Title of Presentation Goes Here</p>
  <p class="t-date">Sunday, February 5, 2023</p>
  <p class="t-foot">© 2023 Corvala.</p>
</section>

<section class="slide col-r" style="top:1104px">
  <div class="photo" role="img" aria-label="Business handshake over contract papers" style="left:40px;top:0;width:214px;height:243px;background:linear-gradient(135deg,#c9ccd3 0%,#8a8f9b 45%,#3d4150 75%,#e8e9ee 100%)"></div>
  <h3 class="abs h-left" style="left:289px;top:58px">Habitant Morbi Tristique<br>Senectus Netus ...</h3>
  <p class="abs role" style="left:289px;top:103px;font-size:8.5px">Sub-Title Goes Here</p>
  <p class="abs p" style="left:289px;top:133px;width:238px">Lorem ipsum dolor sit amet, consectetur adipiscing elit. Vivamus eu dui ex. Curabitur dapibus dignissim dui, in molestie metus feugiat sed. Praesent aliquet lorem ex, eu dapibus odio varius at. Duis eget tellus porta, consequat lacus vitae, venenatis dolor. Nulla facilisi. In et sollicitudin lacus. Donec risus orci, gravida sit amet risus vehicula, aliquet pretium sapien. Nullam sit amet magna non ex bibendum mollis. Nunc vel neque eu augue dignissim congue ut vitae magna. Phasellus eget commodo arcu. Nunc vitae semper dui. Integer venenatis.</p>
  <div class="brand foot-brand"><span class="dot"></span>Corvala</div>
  <div class="foot-rule"></div><p class="copy">Copyright © 2023 Corvala.</p><div class="pg">4</div>
</section>

<!-- row 3 -->
<section class="slide col-l" style="top:1439px">
  <h3 class="h-center">Meet Our Team</h3>
  <div class="round" role="img" aria-label="Team member portrait" style="left:67px;top:71px;width:95px;height:95px;background:radial-gradient(circle at 50% 35%,#d8d2cc,#7d7e84 70%,#2e3038)"></div>
  <div class="round" role="img" aria-label="Team member portrait" style="left:233px;top:71px;width:95px;height:95px;background:radial-gradient(circle at 50% 35%,#d8d2cc,#7d7e84 70%,#2e3038)"></div>
  <div class="round" role="img" aria-label="Team member portrait" style="left:400px;top:71px;width:95px;height:95px;background:radial-gradient(circle at 50% 35%,#d8d2cc,#7d7e84 70%,#2e3038)"></div>
  <div class="abs p-c" style="left:30px;top:179px;width:170px"><p class="name">Lorem Ipsum Dolor</p><p class="role">Lorem ipsum dolor sit amet</p><p class="p" style="margin-top:6px">Lorem ipsum dolor sit amet, consectetur adipiscing elit. Vivamus eu dui ex. Curabitur dapibus dignissim dui, in molestie metus feugiat sed. Praesent aliquet lorem ex, eu dapibus odio varius at.</p></div>
  <div class="abs p-c" style="left:196px;top:179px;width:170px"><p class="name">Lorem Ipsum Dolor</p><p class="role">Lorem ipsum dolor sit amet</p><p class="p" style="margin-top:6px">Lorem ipsum dolor sit amet, consectetur adipiscing elit. Vivamus eu dui ex. Curabitur dapibus dignissim dui, in molestie metus feugiat sed. Praesent aliquet lorem ex, eu dapibus odio varius at.</p></div>
  <div class="abs p-c" style="left:363px;top:179px;width:170px"><p class="name">Lorem Ipsum Dolor</p><p class="role">Lorem ipsum dolor sit amet</p><p class="p" style="margin-top:6px">Lorem ipsum dolor sit amet, consectetur adipiscing elit. Vivamus eu dui ex. Curabitur dapibus dignissim dui, in molestie metus feugiat sed. Praesent aliquet lorem ex, eu dapibus odio varius at.</p></div>
  <div class="brand foot-brand"><span class="dot"></span>Corvala</div>
  <div class="foot-rule"></div><p class="copy">Copyright © 2023 Corvala.</p><div class="pg">5</div>
</section>

<section class="slide col-r" style="top:1439px">
  <div class="photo" role="img" aria-label="Two colleagues working together at a laptop" style="left:0;top:0;width:193px;height:316px;background:linear-gradient(160deg,#7a6a5c 0%,#b39579 35%,#5b4a3e 65%,#2f2a2a 100%)"></div>
  <h3 class="abs h-left" style="left:228px;top:30px">Habitant Morbi Tristique</h3>
  <p class="abs p" style="left:228px;top:64px;width:300px">Praesent aliquet lorem ex, eu dapibus odio varius at. Duis eget tellus porta, consequat lacus vitae, venenatis dolor. Nulla facilisi. In et sollicitudin lacus. Donec risus orci, gravida sit amet risus vehicula, aliquet pretium sapien. Nullam sit amet magna non ex bibendum mollis.</p>
  <div class="round" style="left:224px;top:138px;width:30px;height:30px;background:var(--purple)"><svg width="14" height="14" viewBox="0 0 14 14"><circle cx="7" cy="5.5" r="4" fill="#fff"/><rect x="5" y="9.5" width="4" height="3" rx="1" fill="#fff"/></svg></div>
  <div class="abs" style="left:266px;top:132px;width:110px"><p class="head">Heading</p><p class="p" style="font-size:5.6px;line-height:7px">Curabitur dapibus dignissim dui, in molestie metus feugiat sed. Praesent aliquet lorem ex.</p></div>
  <div class="round" style="left:388px;top:138px;width:30px;height:30px;background:var(--orange)"><svg width="14" height="14" viewBox="0 0 14 14"><circle cx="6" cy="6" r="4" fill="none" stroke="#fff" stroke-width="2"/><line x1="9" y1="9" x2="13" y2="13" stroke="#fff" stroke-width="2"/></svg></div>
  <div class="abs" style="left:430px;top:132px;width:110px"><p class="head">Heading</p><p class="p" style="font-size:5.6px;line-height:7px">Curabitur dapibus dignissim dui, in molestie metus feugiat sed. Praesent aliquet lorem ex.</p></div>
  <div class="round" style="left:224px;top:213px;width:30px;height:30px;background:var(--orange)"><svg width="14" height="14" viewBox="0 0 14 14"><circle cx="7" cy="6" r="4.5" fill="#fff"/><path d="M4 9 L3 13 L7 11 L11 13 L10 9Z" fill="#fff"/></svg></div>
  <div class="abs" style="left:266px;top:207px;width:110px"><p class="head">Heading</p><p class="p" style="font-size:5.6px;line-height:7px">Curabitur dapibus dignissim dui, in molestie metus feugiat sed. Praesent aliquet lorem ex.</p></div>
  <div class="round" style="left:388px;top:213px;width:30px;height:30px;background:var(--purple)"><svg width="14" height="14" viewBox="0 0 14 14"><rect x="1" y="6" width="3" height="7" fill="#fff"/><path d="M5 6 L8 1 Q10 1 9.5 4 L9 6 L13 6 Q13.5 8 12 13 L5 13Z" fill="#fff"/></svg></div>
  <div class="abs" style="left:430px;top:207px;width:110px"><p class="head">Heading</p><p class="p" style="font-size:5.6px;line-height:7px">Curabitur dapibus dignissim dui, in molestie metus feugiat sed. Praesent aliquet lorem ex.</p></div>
  <div class="foot-rule" style="left:240px"></div><p class="copy">Copyright © 2023 Corvala.</p><div class="pg">6</div>
</section>

<!-- row 4 -->
<section class="slide col-l" style="top:1774px">
  <h3 class="h-center">Habitant Morbi Tristique</h3>
  <svg class="abs" style="left:0;top:0" width="563" height="316" viewBox="0 0 563 316">
    <path d="M0 125 H215 V212 H260" fill="none" stroke="#cfcfd4" stroke-width="1"/>
    <path d="M300 212 H345 V125 H563" fill="none" stroke="#cfcfd4" stroke-width="1"/>
  </svg>
  <div class="num" style="left:90px;top:106px;background:var(--purple)">1</div>
  <div class="num" style="left:261px;top:193px;background:var(--orange)">2</div>
  <div class="num" style="left:432px;top:106px;background:#4d4d50">3</div>
  <div class="abs p-c" style="left:200px;top:84px;width:162px"><p class="orange-h">Nullam Sit Amet Magna<br>Non Ex Bibendum</p><p class="p" style="margin-top:5px">Duis eget tellus porta, consequat lacus vitae, venenatis dolor. Nulla facilisi. In et sollicitudin lacus. Donec risus orci, gravida sit amet risus vehicula, aliquet pretium sapien.</p></div>
  <div class="abs p-c" style="left:28px;top:178px;width:162px"><p class="name" style="color:var(--purple)">Nullam Sit Amet Magna<br>Non Ex Bibendum</p><p class="p" style="margin-top:5px">Duis eget tellus porta, consequat lacus vitae, venenatis dolor. Nulla facilisi. In et sollicitudin lacus. Donec risus orci, gravida sit amet risus vehicula, aliquet pretium sapien.</p></div>
  <div class="abs p-c" style="left:370px;top:178px;width:162px"><p class="name" style="color:#3c3c40">Nullam Sit Amet Magna<br>Non Ex Bibendum</p><p class="p" style="margin-top:5px">Duis eget tellus porta, consequat lacus vitae, venenatis dolor. Nulla facilisi. In et sollicitudin lacus. Donec risus orci, gravida sit amet risus vehicula, aliquet pretium sapien.</p></div>
  <div class="brand foot-brand"><span class="dot"></span>Corvala</div>
  <div class="foot-rule"></div><p class="copy">Copyright © 2023 Corvala.</p><div class="pg">7</div>
</section>

<section class="slide col-r" style="top:1774px">
  <h3 class="h-center">Habitant Morbi Tristique</h3>
  <svg class="abs" style="left:0;top:0" width="563" height="316" viewBox="0 0 563 316">
    <circle cx="238" cy="121" r="32" fill="#fff" stroke="var(--purple)" stroke-width="4"/>
    <circle cx="238" cy="121" r="23" fill="var(--purple)"/>
    <circle cx="238" cy="121" r="10" fill="none" stroke="#fff" stroke-width="2"/>
    <path d="M238 115 V121 H243" fill="none" stroke="#fff" stroke-width="2"/>
    <circle cx="324" cy="121" r="32" fill="#fff" stroke="var(--orange)" stroke-width="4"/>
    <circle cx="324" cy="121" r="23" fill="var(--orange)"/>
    <path d="M318 127 L330 115 M326 111 L334 119 L328 125 L320 117Z M316 129 L321 124" fill="#fff" stroke="#fff" stroke-width="2"/>
    <circle cx="238" cy="208" r="32" fill="#fff" stroke="var(--orange)" stroke-width="4"/>
    <circle cx="238" cy="208" r="23" fill="var(--orange)"/>
    <circle cx="238" cy="206" r="8" fill="#fff"/>
    <path d="M233 212 L231 221 L238 217 L245 221 L243 212Z" fill="#fff"/>
    <circle cx="324" cy="208" r="32" fill="#fff" stroke="var(--purple)" stroke-width="4"/>
    <circle cx="324" cy="208" r="23" fill="var(--purple)"/>
    <rect x="314" y="199" width="20" height="18" rx="2" fill="none" stroke="#fff" stroke-width="2"/>
    <line x1="314" y1="204" x2="334" y2="204" stroke="#fff" stroke-width="2"/>
    <path d="M318 208h3M323 208h3M328 208h3M318 212h3M323 212h3M328 212h3" stroke="#fff" stroke-width="2"/>
    <path d="M270 121 H292" stroke="var(--purple)" stroke-width="2"/><path d="M288 117 L293 121 L288 125" fill="none" stroke="var(--orange)" stroke-width="2"/>
    <path d="M238 153 V176" stroke="var(--orange)" stroke-width="2"/>
    <path d="M292 208 H270" stroke="var(--purple)" stroke-width="2"/>
    <path d="M324 176 V153" stroke="var(--orange)" stroke-width="2"/>
  </svg>
  <div class="abs" style="left:36px;top:100px;width:160px;text-align:right"><p class="name" style="font-size:8.5px">Lorem Ipsum Dolor</p><p class="p" style="margin-top:4px">Lorem ipsum dolor sit amet, consectetur adipiscing elit. Vivamus eu dui ex. Curabitur dapibus dignissim dui, in molestie metus</p></div>
  <div class="abs" style="left:374px;top:100px;width:160px"><p class="name" style="font-size:8.5px;color:var(--orange)">Lorem Ipsum Dolor</p><p class="p" style="margin-top:4px">Lorem ipsum dolor sit amet, consectetur adipiscing elit. Vivamus eu dui ex. Curabitur dapibus dignissim dui, in molestie metus</p></div>
  <div class="abs" style="left:36px;top:188px;width:160px;text-align:right"><p class="name" style="font-size:8.5px;color:var(--orange)">Lorem Ipsum Dolor</p><p class="p" style="margin-top:4px">Lorem ipsum dolor sit amet, consectetur adipiscing elit. Vivamus eu dui ex. Curabitur dapibus dignissim dui, in molestie metus</p></div>
  <div class="abs" style="left:374px;top:188px;width:160px"><p class="name" style="font-size:8.5px">Lorem Ipsum Dolor</p><p class="p" style="margin-top:4px">Lorem ipsum dolor sit amet, consectetur adipiscing elit. Vivamus eu dui ex. Curabitur dapibus dignissim dui, in molestie metus</p></div>
  <div class="brand foot-brand"><span class="dot"></span>Corvala</div>
  <div class="foot-rule"></div><p class="copy">Copyright © 2023 Corvala.</p><div class="pg">8</div>
</section>

<!-- row 5 -->
<section class="slide col-l" style="top:2109px">
  <div class="abs" style="left:0;top:0;width:563px;height:64px;background:linear-gradient(90deg,var(--purple) 0%,#8b5d8a 55%,var(--orange) 100%)"></div>
  <h3 class="h-center" style="color:#fff;top:18px">Nullam Sit Amet Magna Non Ex Bibendum</h3>
  <div class="photo" role="img" aria-label="Business handshake" style="left:27px;top:63px;width:152px;height:75px;background:linear-gradient(135deg,#d6d9e0,#7a8090 60%,#e9eaee)"></div>
  <div class="photo" role="img" aria-label="Hands joining puzzle pieces" style="left:205px;top:63px;width:152px;height:75px;background:linear-gradient(135deg,#efe6da,#c49a6c 55%,#5a3b28)"></div>
  <div class="photo" role="img" aria-label="Team meeting around a table" style="left:385px;top:63px;width:152px;height:75px;background:linear-gradient(135deg,#c8c0b8,#7b5e52 55%,#2e2a30)"></div>
  <div class="abs p-c" style="left:27px;top:149px;width:152px"><p class="name">Nullam Sit Amet</p><p class="role">Lorem ipsum dolor sit amet</p></div>
  <div class="abs p-c" style="left:205px;top:149px;width:152px"><p class="name">Praesent Aliquet</p><p class="role">Lorem ipsum dolor sit amet</p></div>
  <div class="abs p-c" style="left:385px;top:149px;width:152px"><p class="name">Pellentesque</p><p class="role">Lorem ipsum dolor sit amet</p></div>
  <ul class="abs list" style="left:36px;top:188px;width:140px"><li>Nunc placerat, arcu nec mattis</li><li>fermentum, nisi mauris convallis</li><li>luctus nunc nisl id ex.</li><li>Nam semper tristique mauris</li><li>vestibulum leo fringilla vel.</li><li>Nulla id augue eleifend, egestas ligula et, consequat massa.</li></ul>
  <ul class="abs list" style="left:214px;top:188px;width:140px"><li>Nunc placerat, arcu nec mattis</li><li>fermentum, nisi mauris convallis</li><li>luctus nunc nisl id ex.</li><li>Nam semper tristique mauris</li><li>vestibulum leo fringilla vel.</li><li>Nulla id augue eleifend, egestas ligula et, consequat massa.</li></ul>
  <ul class="abs list" style="left:394px;top:188px;width:140px"><li>Nunc placerat, arcu nec mattis</li><li>fermentum, nisi mauris convallis</li><li>luctus nunc nisl id ex.</li><li>Nam semper tristique mauris</li><li>vestibulum leo fringilla vel.</li><li>Nulla id augue eleifend, egestas ligula et, consequat massa.</li></ul>
  <div class="brand foot-brand"><span class="dot"></span>Corvala</div>
  <div class="foot-rule"></div><p class="copy">Copyright © 2023 Corvala.</p><div class="pg">9</div>
</section>

<section class="slide col-r" style="top:2109px">
  <h3 class="h-center">Habitant Morbi Tristique Senectus Netus</h3>
  <div class="card" style="left:27px">
    <div class="card-top"><span class="round" style="position:static;width:18px;height:18px;background:var(--purple)"></span><span style="color:var(--purple)">Pellentesque habitant morbi</span></div>
    <p class="head">Heading</p><ul class="list"><li>Lorem Ipsum Dolor Sit Amet, Consectetur Adipiscing Elit.</li><li>Vivamus Eu Dui Ex. Curabitur Dapibus Dignissim Dui</li><li>Molestie Metus Feugiat Sed. Praesent Aliquet Lorem</li><li>Tellus Porta, Consequat Lacus Vitae, Venenatis Dolor</li></ul>
    <p class="head" style="color:var(--purple)">Heading</p><ul class="list"><li>Lorem Ipsum Dolor Sit Amet, Consectetur Adipiscing Elit.</li><li>Vivamus Eu Dui Ex. Curabitur Dapibus Dignissim Dui</li></ul>
  </div>
  <div class="card" style="left:155px">
    <div class="card-top"><span class="round" style="position:static;width:18px;height:18px;background:var(--orange)"></span><span style="color:var(--orange)">Pellentesque habitant morbi</span></div>
    <p class="head">Heading</p><ul class="list"><li>Lorem Ipsum Dolor Sit Amet, Consectetur Adipiscing Elit.</li><li>Vivamus Eu Dui Ex. Curabitur Dapibus Dignissim Dui</li><li>Molestie Metus Feugiat Sed. Praesent Aliquet Lorem</li><li>Tellus Porta, Consequat Lacus Vitae, Venenatis Dolor</li></ul>
    <p class="head" style="color:var(--orange)">Heading</p><ul class="list"><li>Lorem Ipsum Dolor Sit Amet, Consectetur Adipiscing Elit.</li><li>Vivamus Eu Dui Ex. Curabitur Dapibus Dignissim Dui</li></ul>
  </div>
  <div class="card" style="left:284px">
    <div class="card-top"><span class="round" style="position:static;width:18px;height:18px;background:var(--purple)"></span><span style="color:var(--purple)">Pellentesque habitant morbi</span></div>
    <p class="head">Heading</p><ul class="list"><li>Lorem Ipsum Dolor Sit Amet, Consectetur Adipiscing Elit.</li><li>Vivamus Eu Dui Ex. Curabitur Dapibus Dignissim Dui</li><li>Molestie Metus Feugiat Sed. Praesent Aliquet Lorem</li><li>Tellus Porta, Consequat Lacus Vitae, Venenatis Dolor</li></ul>
    <p class="head" style="color:var(--purple)">Heading</p><ul class="list"><li>Lorem Ipsum Dolor Sit Amet, Consectetur Adipiscing Elit.</li><li>Vivamus Eu Dui Ex. Curabitur Dapibus Dignissim Dui</li></ul>
  </div>
  <div class="card" style="left:413px">
    <div class="card-top"><span class="round" style="position:static;width:18px;height:18px;background:var(--orange)"></span><span style="color:var(--orange)">Pellentesque habitant morbi</span></div>
    <p class="head">Heading</p><ul class="list"><li>Lorem Ipsum Dolor Sit Amet, Consectetur Adipiscing Elit.</li><li>Vivamus Eu Dui Ex. Curabitur Dapibus Dignissim Dui</li><li>Molestie Metus Feugiat Sed. Praesent Aliquet Lorem</li><li>Tellus Porta, Consequat Lacus Vitae, Venenatis Dolor</li></ul>
    <p class="head" style="color:var(--orange)">Heading</p><ul class="list"><li>Lorem Ipsum Dolor Sit Amet, Consectetur Adipiscing Elit.</li><li>Vivamus Eu Dui Ex. Curabitur Dapibus Dignissim Dui</li></ul>
  </div>
  <div class="brand foot-brand"><span class="dot"></span>Corvala</div>
  <div class="foot-rule"></div><p class="copy">Copyright © 2023 Corvala.</p><div class="pg">10</div>
</section>

<!-- row 6 -->
<section class="slide col-l" style="top:2444px">
  <div class="photo" role="img" aria-label="Business meeting, tinted purple to orange" style="left:0;top:0;width:281px;height:316px;background:linear-gradient(160deg,var(--purple) 0%,#7e4f8c 40%,#c98a4f 75%,var(--orange) 100%)"></div>
  <h3 class="abs" style="left:20px;top:90px;width:241px;text-align:center;color:#fff;font-size:15.5px;font-weight:600;line-height:17px">Habitant Morbi Tristique Senectus Netus ...</h3>
  <p class="abs p p-c" style="left:30px;top:160px;width:221px;color:#fff">Lorem ipsum dolor sit amet, consectetur adipiscing elit. Vivamus eu dui ex. Curabitur dapibus dignissim dui, in molestie metus feugiat sed. Praesent aliquet lorem ex, eu dapibus odio varius at. Duis eget tellus porta.</p>
  <div class="box-num" style="top:39px">01</div>
  <div class="box-num" style="top:109px">02</div>
  <div class="box-num" style="top:183px">03</div>
  <p class="box-txt" style="top:44px">Arcu nec mattis fermentum, nisi mauris convallis nunc, ut luctus nunc nisl id ex. Nam semper tristique mauris, et vestibulum leo fringilla vel. Nulla id augue eleifend, egestas ligula et, consequat massa. Pellentesque habitant morbi tristique senectus et netus et malesuada fames ac turpis egestas.</p>
  <p class="box-txt" style="top:115px">Arcu nec mattis fermentum, nisi mauris convallis nunc, ut luctus nunc nisl id ex. Nam semper tristique mauris, et vestibulum leo fringilla vel. Nulla id augue eleifend, egestas ligula et, consequat massa. Pellentesque habitant morbi tristique senectus et netus et malesuada fames ac turpis egestas.</p>
  <p class="box-txt" style="top:188px">Arcu nec mattis fermentum, nisi mauris convallis nunc, ut luctus nunc nisl id ex. Nam semper tristique mauris, et vestibulum leo fringilla vel. Nulla id augue eleifend, egestas ligula et, consequat massa. Pellentesque habitant morbi tristique senectus et netus et malesuada fames ac turpis egestas.</p>
  <div class="brand foot-brand"><span class="dot"></span>Corvala</div>
  <div class="foot-rule" style="left:300px"></div><p class="copy">Copyright © 2023 Corvala.</p><div class="pg">11</div>
</section>

<section class="slide col-r" style="top:2444px">
  <h3 class="h-center">Slide Title Goes Here</h3>
  <div class="abs" style="left:240px;top:45px;width:83px;height:3px;background:var(--orange)"></div>
  <svg class="abs" style="left:30px;top:80px" width="510" height="200" viewBox="0 0 510 200" font-family="Poppins, Arial, sans-serif">
    <g stroke="#ececef" stroke-width="1">
      <line x1="16" y1="8" x2="501" y2="8"/><line x1="16" y1="30" x2="501" y2="30"/><line x1="16" y1="52" x2="501" y2="52"/>
      <line x1="16" y1="74" x2="501" y2="74"/><line x1="16" y1="96" x2="501" y2="96"/><line x1="16" y1="118" x2="501" y2="118"/>
      <line x1="16" y1="140" x2="501" y2="140" stroke="#cfcfd4"/>
    </g>
    <g font-size="5" fill="#6a6a70" text-anchor="end">
      <text x="10" y="10">6</text><text x="10" y="32">5</text><text x="10" y="54">4</text><text x="10" y="76">3</text><text x="10" y="98">2</text><text x="10" y="120">1</text><text x="10" y="142">0</text>
    </g>
    <g fill="var(--purple)">
      <rect x="28" y="45.4" width="7" height="94.6"/><rect x="76.5" y="85" width="7" height="55"/><rect x="125" y="63" width="7" height="77"/>
      <rect x="173.5" y="41" width="7" height="99"/><rect x="222" y="58.6" width="7" height="81.4"/><rect x="270.5" y="115.8" width="7" height="24.2"/>
      <rect x="319" y="74" width="7" height="66"/><rect x="367.5" y="107" width="7" height="33"/><rect x="416" y="52" width="7" height="88"/>
      <rect x="464.5" y="27.8" width="7" height="112.2"/>
    </g>
    <g fill="var(--orange)">
      <rect x="36" y="87.2" width="7" height="52.8"/><rect x="84.5" y="45.4" width="7" height="94.6"/><rect x="133" y="96" width="7" height="44"/>
      <rect x="181.5" y="78.4" width="7" height="61.6"/><rect x="230" y="89.4" width="7" height="50.6"/><rect x="278.5" y="69.6" width="7" height="70.4"/>
      <rect x="327" y="69.6" width="7" height="70.4"/><rect x="375.5" y="87.2" width="7" height="52.8"/><rect x="424" y="34.4" width="7" height="105.6"/>
      <rect x="472.5" y="36.6" width="7" height="103.4"/>
    </g>
    <g fill="var(--bar-gray)">
      <rect x="44" y="96" width="7" height="44"/><rect x="92.5" y="96" width="7" height="44"/><rect x="141" y="74" width="7" height="66"/>
      <rect x="189.5" y="30" width="7" height="110"/><rect x="238" y="47.6" width="7" height="92.4"/><rect x="286.5" y="16.8" width="7" height="123.2"/>
      <rect x="335" y="87.2" width="7" height="52.8"/><rect x="383.5" y="82.8" width="7" height="57.2"/><rect x="432" y="107" width="7" height="33"/>
      <rect x="480.5" y="69.6" width="7" height="70.4"/>
    </g>
    <g font-size="5.2" fill="#6a6a70" text-anchor="middle">
      <text x="40" y="152">Category 1</text><text x="88.5" y="152">Category 2</text><text x="137" y="152">Category 3</text>
      <text x="185.5" y="152">Category 4</text><text x="234" y="152">Category 5</text><text x="282.5" y="152">Category 6</text>
      <text x="331" y="152">Category 7</text><text x="379.5" y="152">Category 8</text><text x="428" y="152">Category 9</text>
      <text x="476.5" y="152">Category 10</text>
    </g>
    <g font-size="5" fill="#6a6a70">
      <rect x="214" y="189" width="4" height="4" fill="var(--purple)"/><text x="220" y="193">Series 1</text>
      <rect x="244" y="189" width="4" height="4" fill="var(--orange)"/><text x="250" y="193">Series 2</text>
      <rect x="274" y="189" width="4" height="4" fill="var(--bar-gray)"/><text x="280" y="193">Series 3</text>
    </g>
  </svg>
  <div class="brand foot-brand"><span class="dot"></span>Corvala</div>
  <div class="foot-rule"></div><p class="copy">Copyright © 2023 Corvala.</p><div class="pg">12</div>
</section>

<!-- row 7 -->
<section class="slide col-l" style="top:2779px">
  <h3 class="h-center">Slide Title Goes Here</h3>
  <svg class="abs" style="left:0;top:0" width="563" height="316" viewBox="0 0 563 316" font-family="Poppins, Arial, sans-serif">
    <g transform="rotate(-90 121 164)">
      <circle cx="121" cy="164" r="52" fill="none" stroke="#a7a7ad" stroke-width="14"/>
      <circle cx="121" cy="164" r="52" fill="none" stroke="var(--purple)" stroke-width="14" stroke-dasharray="310.4 326.7"/>
    </g>
    <text x="121" y="171" text-anchor="middle" font-size="20" font-weight="600" fill="var(--purple)">95%</text>
    <g transform="rotate(-90 350 123)">
      <circle cx="350" cy="123" r="23" fill="none" stroke="#d6d6da" stroke-width="4"/>
      <circle cx="350" cy="123" r="23" fill="none" stroke="var(--orange)" stroke-width="4" stroke-dasharray="108.4 144.5"/>
    </g>
    <text x="350" y="126" text-anchor="middle" font-size="9" font-weight="600" fill="var(--orange)">75%</text>
    <g transform="rotate(-90 350 207)">
      <circle cx="350" cy="207" r="23" fill="none" stroke="#a7a7ad" stroke-width="4"/>
      <circle cx="350" cy="207" r="23" fill="none" stroke="var(--orange)" stroke-width="4" stroke-dasharray="36.1 144.5"/>
    </g>
    <text x="350" y="210" text-anchor="middle" font-size="9" font-weight="600" fill="var(--orange)">25%</text>
  </svg>
  <div class="abs" style="left:213px;top:94px;width:80px"><p class="name" style="font-size:12.5px;line-height:14px">Nullam Sit Amet</p><p class="p" style="margin-top:8px;font-size:5.8px;line-height:7.2px">Vivamus eu dui ex. Curabitur dapibus dignissim dui, in molestie metus feugiat sed. Praesent aliquet lorem ex, eu dapibus odio varius at. Duis eget tellus porta, consequat lacus vitae, venenatis dolor. Nulla facilisi. In et sollicitudin lacus.</p></div>
  <div class="abs" style="left:398px;top:100px;width:130px"><p class="orange-h" style="font-size:9px">Nullam Sit Amet</p><p class="p" style="margin-top:3px;font-size:5.8px;line-height:7.2px">Lorem ipsum dolor sit amet, consectetur adipiscing elit. Vivamus eu dui ex. Curabitur dapibus dignissim dui.</p></div>
  <div class="abs" style="left:398px;top:185px;width:130px"><p class="orange-h" style="font-size:9px">Nullam Sit Amet</p><p class="p" style="margin-top:3px;font-size:5.8px;line-height:7.2px">Lorem ipsum dolor sit amet, consectetur adipiscing elit. Vivamus eu dui ex. Curabitur dapibus dignissim dui.</p></div>
  <div class="brand foot-brand"><span class="dot"></span>Corvala</div>
  <div class="foot-rule"></div><p class="copy">Copyright © 2023 Corvala.</p><div class="pg">13</div>
</section>

<section class="slide dark col-r" style="top:2779px">
  <div class="photo" role="img" aria-label="Handshake over a signed contract, tinted purple" style="left:230px;top:0;width:333px;height:297px;background:linear-gradient(90deg,rgba(0,0,0,1) 0%,rgba(58,26,99,.85) 35%,rgba(106,72,160,.8) 65%,rgba(200,192,218,.9) 100%)"></div>
  <div class="brand t-brand" style="color:var(--white)"><span class="dot"></span>Corvala</div>
  <h2 class="t-title" style="top:114px">Thank You!</h2>
  <p class="abs" style="left:44px;top:176px;font-size:10px;font-weight:600">Contact Us</p>
  <svg class="abs" style="left:44px;top:208px" width="10" height="46" viewBox="0 0 10 46">
    <path d="M2 1 L4 1 L5 3.5 L4 4.5 Q5 6.5 6 7 L7 6 L9 7 L9 9 Q4 9 1 3Z" fill="var(--orange)"/>
    <rect x="1" y="17" width="8" height="6" rx="1" fill="none" stroke="var(--orange)" stroke-width="1.2"/>
    <path d="M1 17.5 L5 20.5 L9 17.5" fill="none" stroke="var(--orange)" stroke-width="1"/>
    <circle cx="5" cy="36" r="4" fill="none" stroke="var(--orange)" stroke-width="1.2"/>
    <path d="M1 36 H9 M5 32 Q2.5 36 5 40 Q7.5 36 5 32" fill="none" stroke="var(--orange)" stroke-width=".8"/>
  </svg>
  <p class="abs" style="left:60px;top:209px;font-size:7px">Phone Number Goes Here</p>
  <p class="abs" style="left:60px;top:225px;font-size:7px">E-Mail Address Goes Here</p>
  <p class="abs" style="left:60px;top:241px;font-size:7px">URL Address Goes Here</p>
  <p class="t-foot">© 2023 Corvala.</p>
</section>

</body>
</html>
```